Harbison Projects Promo Brochure

Design a simple ,visually impactful brochure that will articulate our company experience and services to prospective clients.

We need to project to have the following elements / structure:
1. Company Intro
2. Company Services
3. Experience
4. Contact Info
5. Images

I'd like to use icons and imagery as needed to illustrate services and experience.
This brochure will be emailed, so the final version will need to be compressed.

I've uploaded our Owner Rep Services, which has phasing, and services (within each phase), see attached. This info needs to be cleanly added to a brochure.

The "Why Harbison Building Management" doc, copy, needs to be included in the brochure.

Include contact info:
Harbison Projects Services, LLC
214-555-0193
www.harbisonprojgroup.example

Target Market(s)

Restaurants and Hospitality Concepts

Font styles to use
Sans Serif

Colors

Designer to choose colors to be used in the design.

Requirements
Must have
• Very easy to read. Clean.
Information and images should be balanced nicely on the page.

use colors of our logo: red, black, grey, white
Should not have
• Very busy text or images.

```html
<!DOCTYPE html>
<html lang="en">
<head>
<meta charset="utf-8">
<title>Harbison Projects Brochure</title>
<link rel="stylesheet" href="https://fonts.googleapis.com/css2?family=Montserrat:ital,wght@0,500;0,600;0,700;1,500&family=Open+Sans:ital,wght@0,400;0,600;1,400&display=swap">
<style>
:root{
  --red:#c4161c;
  --red-dark:#7d0d12;
  --ink:#1c1c1e;
  --charcoal:#2b2b2e;
  --maroon:#2a1a1d;
  --grey:#6d6e71;
  --grey-light:#d9d9db;
  --paper:#ffffff;
  --stage:#e4e4e6;
}
*{box-sizing:border-box;margin:0;padding:0}
html,body{width:1200px;height:2471px;overflow:hidden;background:var(--stage)}
body{position:relative;font-family:"Open Sans",Arial,sans-serif;color:var(--ink)}
.page{position:absolute;background:var(--paper);overflow:hidden}
.head{font-family:"Montserrat",Arial,sans-serif}

/* cover */
.cover{left:340px;top:50px;width:520px;height:700px}
.cover-photo{position:absolute;inset:0}
.cover-brand{position:absolute;left:360px;top:60px;width:140px;text-align:center}
.brand-mark{display:block;width:54px;height:54px;background:var(--red);margin:0 auto 12px}
.brand-name{font-family:"Montserrat",Arial,sans-serif;font-weight:700;font-size:11px;color:var(--ink);letter-spacing:.3px}
.cover-services{position:absolute;left:22px;top:538px;font-family:"Montserrat",Arial,sans-serif;font-weight:600;font-size:17px;line-height:25px;color:var(--ink);letter-spacing:.4px}
.cover-bar{position:absolute;left:0;top:652px;width:100%;height:30px;background:linear-gradient(90deg,var(--red-dark),var(--red) 60%,#9e1218)}
.cover-url{position:absolute;left:22px;top:6px;display:flex;align-items:center;gap:8px;color:#fff;font-family:"Montserrat",Arial,sans-serif;font-weight:600;font-size:12px}

/* spreads */
.spread{position:absolute;left:60px;width:1080px;height:750px}
.spread-one{top:810px}
.spread-two{top:1620px}
.spread .page{top:0;width:540px;height:750px}
.page-left{left:0}
.page-right{left:540px;box-shadow:inset 10px 0 14px -10px rgba(0,0,0,.25)}

.intro-band{position:absolute;left:0;top:0;width:540px;height:213px;background:linear-gradient(100deg,var(--maroon),#3a2428 55%,#1d1416)}
.intro-brand{position:absolute;left:24px;top:40px;width:150px;text-align:center}
.intro-brand .brand-mark{width:66px;height:66px}
.intro-brand .brand-name{color:#fff;font-size:10px}
.intro-copy{position:absolute;left:196px;top:50px;width:320px;color:#e8e2e3;font-size:7.6px;line-height:11px}
.intro-copy p{margin-bottom:9px}
.band-edge{position:absolute;left:0;width:540px;height:14px}

.section-title{position:absolute;left:22px;top:262px;font-family:"Montserrat",Arial,sans-serif;font-weight:700;font-size:12.5px;color:var(--ink);letter-spacing:.2px}
.section-title::after{content:"";display:block;width:150px;height:2px;background:var(--ink);margin-top:5px}

.reason{position:absolute;left:22px;width:496px;display:flex;gap:12px}
.hex{flex:none;width:34px;height:38px}
.reason h3{font-family:"Montserrat",Arial,sans-serif;font-weight:700;font-size:10px;color:var(--red);margin-bottom:3px}
.reason p{font-size:8px;line-height:11px;color:var(--ink)}
.reason p.aside{color:var(--grey);margin-top:4px}
.reason ul{list-style:none;font-size:8px;line-height:11px;color:var(--grey)}

.spark-photo{position:absolute;left:0;top:485px;width:290px;height:265px}
.purpose{position:absolute;left:290px;top:640px;width:250px;height:110px;background:var(--charcoal);padding:32px 18px 0 22px;font-family:"Montserrat",Arial,sans-serif;font-style:italic;font-weight:500;font-size:9px;line-height:13px;color:var(--red)}

.crew-photo{position:absolute;left:0;top:0;width:540px;height:213px}
.quote-band{position:absolute;left:0;top:637px;width:540px;height:113px;background:linear-gradient(90deg,#2e2e31,#19191b);padding:28px 24px 0 24px;display:flex;gap:18px}
.quote-mark{font-family:"Montserrat",Arial,sans-serif;font-weight:700;font-size:54px;line-height:44px;color:var(--grey)}
.quote-band blockquote{font-style:italic;font-size:8.6px;line-height:12.5px;color:#e2e2e2}
.quote-band cite{display:block;font-style:italic;margin-top:4px;color:#bcbcbc}

/* services page */
.venue-photo{position:absolute;left:0;top:0;width:540px;height:340px}
.services-title{position:absolute;left:22px;top:364px;font-family:"Montserrat",Arial,sans-serif;font-weight:700;font-size:12.5px}
.services-title::after{content:"";display:block;width:90px;height:2px;background:var(--ink);margin-top:5px}
.services-sub{position:absolute;left:22px;top:398px;font-family:"Montserrat",Arial,sans-serif;font-weight:500;font-size:8.6px;color:var(--red)}
.service{position:absolute;left:22px;width:500px;display:flex;gap:12px}
.service-icon{flex:none;width:34px;height:34px}
.service h3{font-family:"Montserrat",Arial,sans-serif;font-weight:600;font-size:8.6px;margin-bottom:2px}
.service ul{list-style:none;font-size:7.8px;line-height:10.6px;color:var(--grey)}
.service li::before{content:"• "}

/* matrix */
.matrix-title{position:absolute;left:22px;top:54px;font-family:"Montserrat",Arial,sans-serif;font-weight:700;font-size:12.5px}
.matrix-title::after{content:"";display:block;width:150px;height:2px;background:var(--ink);margin-top:5px}
.matrix{position:absolute;left:0;top:100px;width:525px;height:640px;display:grid;grid-template-columns:150px 78px 84px 46px 90px 77px;grid-template-rows:16px repeat(19,1fr);font-size:5.6px;line-height:7px}
.matrix .colhead{background:#a7a8ab;color:#fff;font-family:"Montserrat",Arial,sans-serif;font-weight:600;font-size:5.4px;display:flex;align-items:center;justify-content:center;text-transform:uppercase}
.matrix .corner{background:var(--ink)}
.phase-cell{background:var(--ink);color:#fff;font-family:"Montserrat",Arial,sans-serif;font-weight:600;font-size:7px;padding:8px 0 0 8px;position:relative;border-bottom:1px solid #3a3a3d}
.phase-cell svg{position:absolute;left:38px;top:38px;width:46px;height:52px}
.cell{padding:2px 4px;border-bottom:1px solid var(--grey-light);color:#4a4a4d;display:flex;align-items:center}
.cell.shade{background:#f1f1f2}
.milestones{background:#ececed;border-left:1px solid var(--grey-light);padding:22px 4px 0;text-align:center;color:#4a4a4d;font-size:5.6px;line-height:8px;border-bottom:1px solid #fff}
</style>
</head>
<body>

<!-- Cover -->
<section class="page cover">
  <svg class="cover-photo" width="520" height="700" viewBox="0 0 520 700" aria-hidden="false">
    <defs>
      <linearGradient id="dusk" x1="0" y1="0" x2="1" y2="1">
        <stop offset="0" stop-color="#4c5a6b"/>
        <stop offset=".45" stop-color="#3b3a34"/>
        <stop offset="1" stop-color="#23282a"/>
      </linearGradient>
    </defs>
    <polygon points="0,0 254,0 520,300 520,600 0,492" fill="url(#dusk)" role="img" aria-label="Aerial evening view of an outdoor dining village lit with string lights"/>
    <polygon points="244,0 262,0 520,290 520,312" fill="var(--ink)"/>
    <polygon points="268,0 276,0 520,275 520,284" fill="var(--grey)"/>
    <polygon points="0,492 520,600 520,612 0,504" fill="var(--ink)"/>
  </svg>
  <div class="cover-brand">
    <span class="brand-mark"></span>
    <span class="brand-name">HARBISON PROJECTS</span>
  </div>
  <div class="cover-services">DESIGN<br>PROGRAM MENAGMENT<br>PROJECT MENAGMENT<br>CONSTRUCTION MENAGMENT</div>
  <div class="cover-bar">
    <div class="cover-url">
      <svg width="12" height="12" viewBox="0 0 12 12"><circle cx="6" cy="6" r="5" fill="none" stroke="#fff" stroke-width="1.2"/><path d="M1 6h10M6 1c-2.5 3-2.5 7 0 10M6 1c2.5 3 2.5 7 0 10" fill="none" stroke="#fff" stroke-width=".9"/></svg>
      www.harbisonprojgroup.example
    </div>
  </div>
</section>

<!-- Spread one: why -->
<div class="spread spread-one">
  <section class="page page-left">
    <div class="intro-band">
      <div class="intro-brand">
        <span class="brand-mark"></span>
        <span class="brand-name">HARBISON PROJECTS</span>
      </div>
      <div class="intro-copy">
        <p>Harbison Projects Services LLC is a group of Dynamic Professionals with deep histories of managing significant projects inside of the Restaurant, Retail and Entertainment space.</p>
        <p>Competitive Advantage: An intimate knowledge and proven track record of managing Design, Procurement, Architectural, and Construction efforts simultaneously to produce Undeniable Results.</p>
        <p>Extensive Network of Qualified Subcontractor Trades &amp; Vendors.</p>
      </div>
    </div>
    <svg class="band-edge" style="top:206px" viewBox="0 0 540 14" preserveAspectRatio="none"><polygon points="0,0 540,0 540,4 260,14 0,8" fill="var(--red)"/></svg>

    <h2 class="section-title">WHY HARBISON BUILDING MANAGEMENT?</h2>

    <div class="reason" style="top:318px">
      <svg class="hex" viewBox="0 0 34 38"><polygon points="17,1 33,10 33,28 17,37 1,28 1,10" fill="var(--red)"/><path d="M10 26V19M15 26V15M20 26V17M25 26V12" stroke="#fff" stroke-width="2.4"/></svg>
      <div>
        <h3>COST SAVINGS</h3>
        <p>If your concepts' annual project volume is between (1–15) projects, you could save money outsourcing, vs utilizing in-house CM's or PM's.</p>
        <p class="aside">Why? When you compare the compensation package w/ all benefits of a qualified Project Manager with 5+ years of management experience, the per-project cost burden from Harbison is potentially 20-30 % less.</p>
      </div>
    </div>
    <div class="reason" style="top:418px">
      <svg class="hex" viewBox="0 0 34 38"><polygon points="17,1 33,10 33,28 17,37 1,28 1,10" fill="var(--red)"/><circle cx="17" cy="21" r="7" fill="none" stroke="#fff" stroke-width="1.8"/><path d="M17 21V17M15 11h4" stroke="#fff" stroke-width="1.8"/></svg>
      <div>
        <h3>SPEED</h3>
        <p>Most likely, we are going to have much more robust processes and systems in place managing multiple projects simultaneously, at a more dynamic pace.</p>
        <p class="aside">Benefit to You? Projects will move through the life cycle more quickly, efficiently and successfully, with guaranteed outcomes.</p>
      </div>
    </div>

    <svg class="spark-photo" viewBox="0 0 290 265">
      <defs><linearGradient id="spark" x1="0" y1="1" x2="1" y2="0"><stop offset="0" stop-color="#8a4a1c"/><stop offset=".4" stop-color="#2c2624"/><stop offset="1" stop-color="#151314"/></linearGradient></defs>
      <polygon points="0,40 145,0 290,40 290,265 0,265" fill="url(#spark)" role="img" aria-label="Worker in branded gear cutting steel with a grinder, sparks flying"/>
    </svg>
    <div class="purpose">"Our Purpose: Step into high-stakes projects and carry them through Design, Construction, Installation and Development."</div>
  </section>

  <section class="page page-right">
    <svg class="crew-photo" viewBox="0 0 540 213" role="img" aria-label="Site team in hard hats and safety vests reviewing a building under construction">
      <defs><linearGradient id="crew" x1="0" y1="0" x2="0" y2="1"><stop offset="0" stop-color="#c9d2da"/><stop offset=".55" stop-color="#a39684"/><stop offset="1" stop-color="#6d5f4f"/></linearGradient></defs>
      <rect width="540" height="213" fill="url(#crew)"/>
    </svg>
    <svg class="band-edge" style="top:206px" viewBox="0 0 540 14" preserveAspectRatio="none"><polygon points="0,0 540,0 540,8 280,14 0,4" fill="var(--red)"/></svg>

    <h2 class="section-title">WHY HARBISON BUILDING MANAGEMENT?</h2>

    <div class="reason" style="top:318px">
      <svg class="hex" viewBox="0 0 34 38"><polygon points="17,1 33,10 33,28 17,37 1,28 1,10" fill="var(--red)"/><circle cx="17" cy="15" r="4" fill="#fff"/><path d="M9 28c1-6 15-6 16 0z" fill="#fff"/></svg>
      <div>
        <h3>INTEGRITY</h3>
        <p>Because we are outsourced, we will push information faster, and communicate at a much higher level than an internal resource.</p>
        <p class="aside">Why? Our value add, is your piece of mind and delivering results. We have a long term vision and strategy, and we are only as good as our last project. We have to keep delivering, while maintaining a high level experience to our customers so that we can thrive and grow.</p>
      </div>
    </div>
    <div class="reason" style="top:420px">
      <svg class="hex" viewBox="0 0 34 38"><polygon points="17,1 33,10 33,28 17,37 1,28 1,10" fill="var(--red)"/><rect x="9" y="12" width="16" height="11" rx="1" fill="none" stroke="#fff" stroke-width="1.8"/><path d="M7 27h20" stroke="#fff" stroke-width="2"/></svg>
      <div>
        <h3>TECHNOLOGY</h3>
        <p>We utilize the latest project management software platforms to ensure high level collaboration, accountability and information transfer.</p>
        <ul><li>• FieldBoard</li><li>• GridSheets</li></ul>
      </div>
    </div>
    <div class="reason" style="top:520px">
      <svg class="hex" viewBox="0 0 34 38"><polygon points="17,1 33,10 33,28 17,37 1,28 1,10" fill="var(--red)"/><path d="M9 27V16l8-5 8 5v11M13 27v-6h8v6" fill="none" stroke="#fff" stroke-width="1.8"/></svg>
      <div>
        <h3>EXPERIENCE</h3>
        <p>Put simply, our team has managed hundreds of projects from restaurant, retail, commercial, warehouse, and government / military logistics - nationwide, and overseas.</p>
        <p class="aside">What does this mean to you? You get the benefit of "best practices" we've acquired from partnering with other industry leading concepts and organizations.</p>
      </div>
    </div>

    <div class="quote-band">
      <span class="quote-mark">“</span>
      <blockquote>"Marcus's ability to manage multiple projects simultaneously is impressive. His approach is straightforward and he always tries to figure out ways to accomplish the design we set forth"
        <cite>- Dana Whitfield | Whitfield Design</cite>
      </blockquote>
    </div>
  </section>
</div>

<!-- Spread two: services and matrix -->
<div class="spread spread-two">
  <section class="page page-left">
    <svg class="venue-photo" viewBox="0 0 540 340">
      <defs><linearGradient id="venue" x1="0" y1="0" x2="0" y2="1"><stop offset="0" stop-color="#1d3a6e"/><stop offset=".6" stop-color="#4a3a48"/><stop offset="1" stop-color="#8a6a52"/></linearGradient></defs>
      <polygon points="0,0 540,0 540,270 300,330 0,300" fill="url(#venue)" role="img" aria-label="Restaurant with a zig-zag red steel canopy photographed at twilight"/>
      <polygon points="0,300 300,330 540,270 540,282 300,340 0,310" fill="var(--ink)"/>
    </svg>

    <h2 class="services-title">SERVICES</h2>
    <p class="services-sub">GENERAL CONSTRUCTION + PROGRAM MANAGEMENT + DESIGN + OWNER REP</p>

    <div class="service" style="top:440px">
      <svg class="service-icon" viewBox="0 0 34 34"><circle cx="17" cy="17" r="16" fill="none" stroke="var(--ink)" stroke-width="1.4"/><circle cx="17" cy="13" r="3.4" fill="var(--ink)"/><circle cx="9.5" cy="15" r="2.6" fill="var(--ink)"/><circle cx="24.5" cy="15" r="2.6" fill="var(--ink)"/><path d="M11 24c0-5 12-5 12 0z M5 24c0-4 7-4 7-1z M22 23c0-3 7-3 7 1z" fill="var(--ink)"/></svg>
      <div>
        <h3>PROGRAM MANAGEMENT</h3>
        <ul>
          <li>Develop Comprehensive Scopes of Work For Entire Project Team</li>
          <li>Selection and Management of Design, Engineering, Construction, and Procurement professionals</li>
          <li>Accurate Front-End Planning &amp; Forecasts</li>
          <li>Management of Total Development Budget and Schedule</li>
          <li>Preparing of Bid Packages, and Managing the Bid Process</li>
          <li>Providing Traditional Construction Management Services</li>
        </ul>
      </div>
    </div>
    <div class="service" style="top:548px">
      <svg class="service-icon" viewBox="0 0 34 34"><circle cx="17" cy="17" r="16" fill="none" stroke="var(--ink)" stroke-width="1.4"/><path d="M17 7l7 17H10z" fill="var(--ink)"/><path d="M8 25h18" stroke="var(--ink)" stroke-width="2"/><path d="M13 18h8" stroke="#fff" stroke-width="1.4"/></svg>
      <div>
        <h3>PRE-CONSTRUCTION / DESIGN PHASE</h3>
        <ul>
          <li>Scope definition and management</li>
          <li>Establishment and maintenance of communications procedures</li>
          <li>Budget development</li>
          <li>Master schedule development - CPM Scheduling</li>
          <li>Site selection assistance</li>
        </ul>
      </div>
    </div>
    <div class="service" style="top:642px">
      <svg class="service-icon" viewBox="0 0 34 34"><circle cx="17" cy="17" r="16" fill="none" stroke="var(--ink)" stroke-width="1.4"/><rect x="9" y="10" width="16" height="15" rx="1" fill="none" stroke="var(--ink)" stroke-width="1.6"/><path d="M9 14h16M13 8v4M21 8v4" stroke="var(--ink)" stroke-width="1.6"/></svg>
      <div>
        <h3>SCHEDULING</h3>
        <ul>
          <li>Master program schedules</li>
          <li>Design phase schedules</li>
          <li>Construction phase schedules</li>
          <li>Completion and turnaround schedules</li>
          <li>Window and look-ahead schedules</li>
          <li>Recovery schedules</li>
        </ul>
      </div>
    </div>
  </section>

  <section class="page page-right">
    <h2 class="matrix-title">OWNER REPRESENTATIVE + CONSTRUCTION MANAGEMENT MATRIX</h2>
    <div class="matrix">
      <div class="corner"></div>
      <div class="colhead">Service</div>
      <div class="colhead">Action / Deliverable</div>
      <div class="colhead">Tool</div>
      <div class="colhead">Collaboration</div>
      <div class="colhead">Milestones</div>

      <div class="phase-cell" style="grid-row:2 / span 5">PLANNING
        <svg viewBox="0 0 46 52"><polygon points="23,1 45,13 45,39 23,51 1,39 1,13" fill="var(--red)"/><path d="M14 24a9 9 0 0 1 18 0z" fill="#fff"/><path d="M12 25h22" stroke="#fff" stroke-width="2"/><circle cx="23" cy="31" r="5" fill="#fff"/></svg>
      </div>
      <div class="cell">Site Evaluation</div><div class="cell">Site report</div><div class="cell">Shared Doc</div><div class="cell">Broker, Owner</div>
      <div class="milestones" style="grid-column:6;grid-row:2 / span 5">Owner approves scope<br>Site selected<br>Design team engaged</div>
      <div class="cell shade">Project Scope Development</div><div class="cell shade">Project plan + scope</div><div class="cell shade">Shared Doc</div><div class="cell shade">Owner, Design lead</div>
      <div class="cell">Architect / Engineer Selection</div><div class="cell">Design team qualified</div><div class="cell">Shared Sheet</div><div class="cell">Owner, Architect</div>
      <div class="cell shade">Conceptual Budgeting</div><div class="cell shade">Conceptual budget</div><div class="cell shade">Shared Sheet</div><div class="cell shade">Owner, Finance</div>
      <div class="cell">Consultant Management</div><div class="cell">Consultant tracking</div><div class="cell">Online</div><div class="cell">Weekly calls</div>

      <div class="phase-cell" style="grid-row:7 / span 6">PRECONSTRUCTION
        <svg viewBox="0 0 46 52"><polygon points="23,1 45,13 45,39 23,51 1,39 1,13" fill="var(--red)"/><path d="M14 24a9 9 0 0 1 18 0z" fill="#fff"/><path d="M12 25h22" stroke="#fff" stroke-width="2"/><circle cx="23" cy="31" r="5" fill="#fff"/></svg>
      </div>
      <div class="cell">CM Selection</div><div class="cell">Bid leveling</div><div class="cell">Shared Doc</div><div class="cell">Owner, CM</div>
      <div class="milestones" style="grid-column:6;grid-row:7 / span 6">Budget approved<br>Schedule approved<br>Permit issued<br>GC under contract</div>
      <div class="cell shade">Budgeting</div><div class="cell shade">Detailed budget</div><div class="cell shade">Shared Doc</div><div class="cell shade">Owner review</div>
      <div class="cell">Procurement Management</div><div class="cell">Procurement log</div><div class="cell">Shared Sheet</div><div class="cell">Vendors, Owner</div>
      <div class="cell shade">Value Engineering</div><div class="cell shade">VE options log</div><div class="cell shade">Shared Doc</div><div class="cell shade">Design team</div>
      <div class="cell">Critical Path Scheduling</div><div class="cell">Master schedule</div><div class="cell">Shared Sheet</div><div class="cell">All parties</div>
      <div class="cell shade">GC Bidding</div><div class="cell shade">GC comparison</div><div class="cell shade">Shared Doc</div><div class="cell shade">Owner, GC</div>

      <div class="phase-cell" style="grid-row:13 / span 8">CONSTRUCTION
        <svg viewBox="0 0 46 52"><polygon points="23,1 45,13 45,39 23,51 1,39 1,13" fill="var(--red)"/><rect x="12" y="16" width="22" height="10" fill="none" stroke="#fff" stroke-width="2"/><path d="M16 26v10M30 26v10M15 16l6 10M23 16l6 10" stroke="#fff" stroke-width="2"/></svg>
      </div>
      <div class="cell">Preconstruction Meetings</div><div class="cell">Pre-con notes</div><div class="cell">Shared Doc</div><div class="cell">GC, Owner</div>
      <div class="milestones" style="grid-column:6;grid-row:13 / span 8">Substantial completion<br>Punch list<br>Turnover<br>Grand opening</div>
      <div class="cell shade">Supervision</div><div class="cell shade">Site walks</div><div class="cell shade">Online</div><div class="cell shade">Weekly</div>
      <div class="cell">Schedule Management</div><div class="cell">Weekly updates</div><div class="cell">Shared Sheet</div><div class="cell">GC, Owner</div>
      <div class="cell shade">Project Reporting</div><div class="cell shade">Owner reports</div><div class="cell shade">Shared Doc</div><div class="cell shade">Weekly</div>
      <div class="cell">Document Management</div><div class="cell">Drawing logs</div><div class="cell">Online</div><div class="cell">Design team</div>
      <div class="cell shade">Site Visits</div><div class="cell shade">Photo reports</div><div class="cell shade">Shared Doc</div><div class="cell shade">Owner</div>
      <div class="cell">Pay App Review</div><div class="cell">Invoice review</div><div class="cell">Shared Sheet</div><div class="cell">Finance</div>
      <div class="cell shade">Closeout + Handover</div><div class="cell shade">Punch list, O&amp;M</div><div class="cell shade">Shared Doc</div><div class="cell shade">All parties</div>
    </div>
  </section>
</div>

</body>
</html>
```